Velmora EIRL Business Card Design Project

We need a business card design for a New Business Intelligence Consultant. We bring a complete service to the client from first consulting meeting to help desk and system improvement.

I will upload the company logo and I like to use the logo colors on the card. Feel free to use all logo components on the design, for example one side with the black logo using complete card and the other side only the red shape (is an example, feel absolutely free :)).

The principal idea is to sell a professional service and a modern company.

Target Market(s)

IT Business Intelligence Clients

Industry/Entity Type

Professional Service

Requirements
Nice to have
• - Use the logo colors and minimize white sections.
- Rounded borders
Should not have
• I don't want to see any references to people working on a meeting or office photos or any computers related logos.

```html
<!DOCTYPE html>
<html lang="es">
<head>
<meta charset="utf-8">
<title>Velmora EIRL – Tarjeta de presentación</title>
<link rel="stylesheet" href="https://fonts.googleapis.com/css2?family=Mulish:wght@400;700&display=swap">
<style>
  :root {
    --stage: #3a3a3a;
    --card: #2b2b2b;
    --card-edge: #232323;
    --red: #e21d24;
    --text-light: #d9d9d9;
    --text-mid: #a8a8a8;
    --logo-grey: #bdbdbd;
  }
  * { box-sizing: border-box; margin: 0; padding: 0; }
  html, body {
    width: 1200px; height: 874px; overflow: hidden;
    background: var(--stage);
    font-family: "Mulish", sans-serif;
  }
  .stage {
    width: 1200px; height: 874px;
    display: flex; align-items: center; justify-content: center; gap: 60px;
  }
  .card {
    position: relative;
    width: 520px; height: 300px;
    border-radius: 22px;
    background: var(--card);
    box-shadow: 0 10px 30px rgba(0,0,0,.35);
    overflow: hidden;
  }
  /* Front */
  .front-brand {
    position: absolute; left: 70px; top: 110px;
    display: flex; align-items: center; gap: 18px;
  }
  .brand-square { width: 42px; height: 42px; background: var(--logo-grey); }
  .brand-name {
    font-size: 58px; font-weight: 400; color: var(--red);
    letter-spacing: 1px; line-height: 1;
  }
  .front-band { position: absolute; left: 0; bottom: 0; width: 520px; height: 56px; }
  .front-url {
    position: absolute; right: 40px; bottom: 17px;
    font-size: 16px; color: #f3c9ca; letter-spacing: .5px;
  }
  /* Back */
  .back-block {
    position: absolute; left: 40px; top: 50px;
    width: 200px; height: 200px; background: var(--red);
  }
  .back-info { position: absolute; left: 270px; top: 48px; width: 220px; }
  .person-name { font-size: 21px; font-weight: 700; color: var(--text-light); }
  .person-role { font-size: 15px; color: var(--text-mid); margin-top: 3px; }
  .rule { height: 2px; background: var(--red); margin: 12px 0 16px; }
  .contact { list-style: none; }
  .contact li {
    display: flex; align-items: flex-start; gap: 9px;
    font-size: 12.5px; line-height: 1.35; color: var(--text-mid); margin-bottom: 6px;
  }
  .contact svg { flex: none; width: 12px; height: 12px; margin-top: 2px; fill: var(--text-mid); }
</style>
</head>
<body>
<main class="stage">
  <section class="card card-front" aria-label="Anverso">
    <div class="front-brand">
      <span class="brand-square"></span>
      <span class="brand-name">velmora</span>
    </div>
    <svg class="front-band" viewBox="0 0 520 56" aria-hidden="true">
      <path d="M60 0 H520 V56 H0 C30 56 40 0 60 0 Z" fill="var(--red)"/>
    </svg>
    <span class="front-url">www.velmora.cl</span>
  </section>

  <section class="card card-back" aria-label="Reverso">
    <div class="back-block"></div>
    <div class="back-info">
      <h1 class="person-name">Tomás Ferrer L.</h1>
      <p class="person-role">Gerente General</p>
      <div class="rule"></div>
      <ul class="contact">
        <li><svg viewBox="0 0 12 12"><path d="M2.5 0.5 L4.5 3 L3.3 4.4 C4 6 5.8 7.8 7.6 8.7 L9 7.5 L11.5 9.5 L10 11.5 C5 11 1 7 0.5 2 Z"/></svg>+56 (9) 4821 6630</li>
        <li><svg viewBox="0 0 12 12"><path d="M0 2 H12 V10 H0 Z M0.8 2.6 L6 6.6 L11.2 2.6 V3.6 L6 7.6 L0.8 3.6 Z" fill-rule="evenodd"/></svg>tomas@velmora.cl</li>
        <li><svg viewBox="0 0 12 12"><circle cx="6" cy="6" r="5.5" fill="none" stroke="var(--text-mid)"/><path d="M0.5 6 H11.5 M6 0.5 C3 3 3 9 6 11.5 C9 9 9 3 6 0.5" fill="none" stroke="var(--text-mid)" stroke-width=".8"/></svg>www.velmora.cl</li>
        <li><svg viewBox="0 0 12 12"><path d="M6 0 C3 0 1.5 2 1.5 4.3 C1.5 7 6 12 6 12 C6 12 10.5 7 10.5 4.3 C10.5 2 9 0 6 0 Z M6 2.5 A1.8 1.8 0 1 0 6 6.1 A1.8 1.8 0 1 0 6 2.5 Z" fill-rule="evenodd"/></svg>Av. Los Aromos 418 Of. 305, Providencia, Santiago</li>
      </ul>
    </div>
  </section>
</main>
</body>
</html>
```